Heating and Cooling Company mobile website

We need a website specifically designed for a viewing on a mobile device.

We serve the northern New Jersey heating, cooling and electrical residential market.

The goal is the drive traffic to the site by using Brindle Pay Per click. People will be searching for an HVAC contractor, and they land on our page. They need to get key info quickly without all the clutter of a desktop type of site.

Target Market(s)

Homeowners

Industry/Entity Type

Hvac

Coding

Coded - Design and coding required

Number of Pages Required

5+ page

Font styles to use
Serif

Requirements
Must have
• View attachments to see samples of the desktop version. It must have a similar color scheme
• The copy of the website is also attached
Nice to have
• Would like it to have a sort of Quello feel to it. Make it seem like its an app that people are using and that its exciting to be on the website. It would be nice to have a page where customers can book appointments

```html
<!DOCTYPE html>
<html lang="en">
<head>
<meta charset="utf-8">
<title>Hearthwell Comfort – Mobile</title>
<link href="https://fonts.googleapis.com/css2?family=Tinos:ital,wght@0,400;0,700;1,400;1,700&family=Open+Sans:wght@400;600;700&display=swap" rel="stylesheet">
<style>
  :root{
    --red:#b3202a;
    --red-dark:#8e1820;
    --orange:#f39a1c;
    --ink:#111111;
    --grey:#555555;
    --paper:#ffffff;
    --page:#ececec;
    --footer-top:#3a3a3a;
    --footer-bottom:#0d0d0d;
    --dark-btn:#2b2b2b;
  }
  *{box-sizing:border-box;margin:0;padding:0}
  html,body{width:857px;height:1200px;overflow:hidden;background:var(--page)}
  body{font-family:"Open Sans",Arial,sans-serif;color:var(--ink)}
  .page{position:relative;width:857px;height:1200px;background:var(--paper);overflow:hidden}

  .header{position:absolute;top:0;left:0;width:100%;height:160px}
  .social{position:absolute;left:128px;top:40px;display:flex;gap:10px}
  .social span{width:20px;height:20px;border-radius:50%;background:var(--orange);display:block}
  .brand{position:absolute;left:50%;top:44px;transform:translateX(-50%);font-family:"Tinos",serif;font-weight:700;font-size:34px;color:var(--red);white-space:nowrap;display:flex;align-items:center;gap:12px}
  .brand i{width:22px;height:22px;background:var(--red);border-radius:50%;display:block}
  .menu{position:absolute;right:120px;top:44px;width:28px}
  .menu span{display:block;height:3px;background:var(--ink);margin-bottom:6px}
  .rule{position:absolute;left:0;width:100%;height:5px;background:var(--red)}

  .hero{position:absolute;left:120px;top:168px;width:617px;height:295px;background:radial-gradient(circle at 72% 45%,#f6e2b0 0%,#c89a58 22%,#6d5236 55%,#2f251c 100%)}
  .hero h1{position:absolute;top:16px;left:0;width:100%;text-align:center;font-family:"Tinos",serif;font-style:italic;font-weight:700;font-size:37px;line-height:42px;color:#fff}
  .open{position:absolute;left:148px;top:204px;display:flex;height:44px}
  .open .time{background:var(--orange);color:#fff;font-weight:700;font-size:22px;padding:0 14px;line-height:44px}
  .open .time small{font-size:15px}
  .open .state{background:#222;color:#fff;font-weight:700;font-size:14px;padding:0 22px;line-height:44px}

  .quote{position:absolute;top:477px;left:0;width:100%;text-align:center;font-family:"Tinos",serif;font-style:italic;font-size:16px;line-height:20px;color:var(--grey)}

  .tabs{position:absolute;top:543px;left:120px;width:617px;height:64px;display:flex;border-top:1px solid #e3e3e3;border-bottom:1px solid #e3e3e3}
  .tabs a{flex:1;text-align:center;line-height:64px;font-size:14px;color:var(--ink);text-decoration:none}
  .tabs a.active{background:var(--orange);color:#fff;flex:0 0 102px;margin-left:10px}

  .btn{position:absolute;left:50%;transform:translateX(-50%);width:214px;height:22px;background:var(--dark-btn);color:#fff;font-size:9px;font-weight:600;text-align:center;line-height:22px;letter-spacing:.5px}

  .band{position:absolute;top:654px;left:0;width:100%;height:42px;background:var(--red);color:#fff;text-align:center;font-family:"Tinos",serif;font-style:italic;font-weight:700;font-size:34px;line-height:42px}
  .services{position:absolute;top:712px;left:0;width:100%;text-align:center;font-family:"Tinos",serif;font-style:italic;font-weight:700;font-size:42px;line-height:44px;list-style:none}

  .footer{position:absolute;top:950px;left:0;width:100%;height:250px;background:linear-gradient(var(--footer-top),var(--footer-bottom));color:#fff}
  .contact{position:absolute;left:148px;top:40px;font-size:10px;line-height:20px}
  .contact b{font-weight:600}
  .contact em{color:var(--orange);font-style:normal}
  .contact svg{vertical-align:middle;margin-right:6px}
  .follow{position:absolute;left:383px;top:40px;font-size:10px;text-align:center;width:90px}
  .follow div{display:flex;gap:14px;justify-content:center;margin-top:10px}
  .follow span{width:18px;height:18px;background:var(--orange);display:block}
  .links{position:absolute;left:592px;top:44px;font-size:10px;line-height:22px;list-style:none}
  .links em{color:var(--orange);font-style:normal}
  .nav{position:absolute;left:120px;top:178px;width:617px;border-top:1px solid #555;display:flex;justify-content:space-around;padding-top:12px;font-size:10px;color:#ccc}
</style>
</head>
<body>
<div class="page">
  <header class="header">
    <div class="social"><span></span><span></span><span></span></div>
    <div class="brand"><i></i>Hearthwell Comfort</div>
    <div class="menu"><span></span><span></span><span></span></div>
  </header>
  <div class="rule" style="top:160px"></div>

  <section class="hero" role="img" aria-label="Photo of a glowing vintage light bulb">
    <h1>The Best Way To Live In New Jersey<br>Is With Comfort!</h1>
    <div class="open"><div class="time">00:06 <small>hrs.</small></div><div class="state">YES, we are OPEN</div></div>
  </section>

  <p class="quote">"Seriously, don't be afraid to call at any time, we live for this,<br>just give us a min to get some coffee on the way over"</p>

  <nav class="tabs">
    <a class="active">Heating</a><a>Air Conditioning</a><a>Electrical</a><a>Ventilation</a>
  </nav>
  <div class="btn" style="top:619px">VIEW ALL</div>

  <div class="rule" style="top:646px;height:3px"></div>
  <h2 class="band">Our Services</h2>
  <ul class="services">
    <li>Heating</li><li>Air conditioning</li><li>Electrical</li><li>Ventilation</li>
  </ul>
  <div class="btn" style="top:912px">VIEW ALL</div>
  <div class="rule" style="top:943px;height:4px"></div>

  <footer class="footer">
    <div class="contact">
      <b>CONTACT US <em>TODAY!</em></b><br>
      <svg width="12" height="12" viewBox="0 0 12 12"><circle cx="6" cy="6" r="6" fill="#f39a1c"/><path d="M4 3l1 2-1 1 2 2 1-1 2 1-1 2C5 10 2 7 2 4z" fill="#fff"/></svg>555-0142-880<br>
      <svg width="12" height="12" viewBox="0 0 12 12"><circle cx="6" cy="6" r="6" fill="#f39a1c"/><rect x="3" y="4" width="6" height="4" fill="#fff"/></svg>hello@<em>hearthwell.co</em>
    </div>
    <div class="follow">Like · Follow us<div><span></span><span></span></div></div>
    <ul class="links">
      <li>Heating <em>service</em></li>
      <li>Air conditioning <em>service</em></li>
      <li>Electrical <em>service</em></li>
      <li>Ventilation <em>service</em></li>
    </ul>
    <div class="nav"><span>Home</span><span>About Us</span><span>Our Services</span><span>FAQ</span><span>Contact Us</span></div>
  </footer>
</div>
</body>
</html>
```